Quiet Harbour is a Counseling company and needs a website design.

I need a website design for my Counseling company based in Singapore. I provide counseling and other related services through therapy. I website is my front face and want it to represent my personality and the name of the company itself. My company represents non judgement, compassionate and a safe environment for people to come by and talk about their issues/problems.

I want the website to be something connected to nature earth like a perfect Sanctuary. When a person sees my website i want to immediately feel a piece of calmness and peace. This is essential to me.

Target Market(s)

All age groups above 13 years of age

Industry/Entity Type

It Company

Requirements
Must have
• Not too flashy and must connect to any common man irrespective of age
Should not have
• Good calm color concept

```html
<!DOCTYPE html>
<html lang="en">
<head>
<meta charset="utf-8">
<title>Quiet Harbour</title>
<link rel="stylesheet" href="https://fonts.googleapis.com/css2?family=Comic+Neue:wght@700&family=Noto+Sans:wght@400;700&family=Noto+Serif:ital@0;1&display=swap">
<style>
  :root {
    --page-bg: #b2dd91;
    --page-swoosh: #c6e7ab;
    --frame: #7fb356;
    --white: #ffffff;
    --title: #1f3a0e;
    --olive: #6f8500;
    --olive-light: #8a9e00;
    --ink: #1a1a1a;
    --tab: #6cb33a;
    --menu-active-top: #c8ec9e;
    --menu-active-bottom: #8fcf62;
    --footer: #e8f56b;
    --rss: #f08a24;
    --note: #111111;
  }
  * { margin: 0; padding: 0; box-sizing: border-box; }
  html, body { width: 1156px; height: 1200px; overflow: hidden; }
  body {
    position: relative;
    background: var(--page-bg);
    font-family: "Noto Sans", sans-serif;
    color: var(--ink);
  }
  .swoosh { position: absolute; left: 0; top: 0; }
  .site {
    position: absolute; left: 42px; top: 41px; width: 1076px; height: 1134px;
    background: var(--white);
    border: 3px solid var(--frame);
    border-radius: 12px;
    overflow: hidden;
    box-shadow: 0 2px 6px rgba(60, 100, 30, .35);
  }
  .header {
    position: absolute; left: 0; top: 0; width: 100%; height: 273px;
  }
  .header-photo {
    position: absolute; inset: 0;
    background:
      radial-gradient(ellipse 260px 200px at 220px 120px, #3f9a1c 0%, rgba(80,160,30,.6) 55%, rgba(0,0,0,0) 100%),
      radial-gradient(ellipse 500px 260px at 820px 80px, #f0f7b0 0%, rgba(220,240,130,.5) 60%, rgba(0,0,0,0) 100%),
      linear-gradient(100deg, #6fb52a 0%, #b6dc4a 45%, #d8ec72 75%, #c4e25a 100%);
  }
  .site-title {
    position: absolute; left: 0; right: 0; top: 122px; padding-left: 460px;
    font-family: "Comic Neue", cursive; font-weight: 700;
    font-size: 58px; letter-spacing: 2px; color: var(--title); line-height: 1;
  }
  .site-title span { position: absolute; left: 370px; width: 580px; text-align: center; }
  .site-slogan {
    position: absolute; left: 370px; width: 580px; top: 200px; text-align: center;
    font-weight: 700; font-size: 26px; color: var(--title);
  }
  .topnav {
    position: absolute; left: 0; top: 273px; width: 100%; height: 53px;
  }
  .topnav a {
    position: absolute; top: 5px; height: 44px; line-height: 44px;
    font-size: 20px; color: var(--olive); text-decoration: none; text-align: center;
  }
  .topnav a.current { background: var(--tab); color: var(--ink); border-radius: 4px 4px 0 0; }
  .topnav .sep { position: absolute; top: 4px; height: 46px; border-left: 1px dotted #b9c47a; }

  .sidebar h2 {
    position: absolute; font-size: 23px; font-weight: 700; color: var(--ink);
  }
  .menu a {
    position: absolute; font-size: 20px; color: var(--ink); text-decoration: none; line-height: 1;
  }
  .menu a.sub { color: var(--olive-light); }
  .menu .active-bg {
    position: absolute; left: 12px; top: 429px; width: 245px; height: 41px;
    background: linear-gradient(var(--menu-active-top), var(--menu-active-bottom));
    border: 1px solid #7dbb50; border-radius: 3px;
  }
  .block-text {
    position: absolute; left: 18px; width: 236px; font-size: 20px; line-height: 27px; color: var(--ink);
  }

  .main { font-family: "Noto Serif", serif; }
  .feature-photo {
    position: absolute; left: 312px; top: 374px; width: 342px; height: 233px;
    background: linear-gradient(#4f95d8 0%, #9cc9ee 42%, #5db7d8 58%, #1f8fc4 100%);
  }
  .intro {
    position: absolute; left: 662px; top: 364px; width: 380px;
    font-size: 20.5px; line-height: 28.5px; color: var(--olive);
  }
  .intro p + p { margin-top: 14px; }
  .read-more {
    position: absolute; left: 301px; top: 625px; font-size: 20.5px; color: var(--olive); text-decoration: none;
  }
  .points {
    position: absolute; left: 345px; top: 697px; width: 310px; list-style: none;
    font-size: 20.5px; line-height: 28.5px; color: var(--ink);
  }
  .points li { position: relative; margin-bottom: 5px; }
  .points li::before {
    content: ""; position: absolute; left: -16px; top: 10px; width: 8px; height: 8px;
    border: 1px solid #8a8a8a;
  }
  .quote {
    position: absolute; left: 740px; top: 697px; width: 300px;
    font-style: italic; font-size: 20.5px; line-height: 28.5px; color: var(--ink);
  }
  .quote-mark { position: absolute; left: 702px; top: 700px; }

  .footer {
    position: absolute; left: 0; bottom: 0; width: 100%; height: 61px; background: var(--footer);
    text-align: center; font-size: 16.5px; line-height: 22px; padding-top: 6px; padding-left: 14px;
  }
  .footer a { color: var(--ink); text-decoration: none; }
  .feed-icon {
    position: absolute; left: 8px; top: 9px; width: 42px; height: 42px;
    background: var(--rss); border-radius: 6px;
  }
  .notes { position: absolute; left: 0; top: 0; pointer-events: none; }
</style>
</head>
<body>
  <svg class="swoosh" width="1156" height="80" aria-hidden="true">
    <path d="M0 55 C120 10 260 2 420 0 L0 0 Z" fill="var(--page-swoosh)"/>
  </svg>

  <div class="site">
    <header class="header">
      <div class="header-photo" role="img" aria-label="Fresh green leaves on a sunlit branch"></div>
      <h1 class="site-title"><span>Enter Site Title</span></h1>
      <p class="site-slogan">Enter Site Slogan</p>
    </header>

    <nav class="topnav">
      <a class="current" href="#" style="left:5px;width:121px;">Home</a>
      <span class="sep" style="left:130px"></span>
      <a href="#" style="left:130px;width:170px;">About Me</a>
      <span class="sep" style="left:300px"></span>
      <a href="#" style="left:300px;width:199px;">Consultation</a>
      <span class="sep" style="left:499px"></span>
      <a href="#" style="left:499px;width:176px;">Resources</a>
      <span class="sep" style="left:675px"></span>
      <a href="#" style="left:675px;width:184px;">Contact Me</a>
    </nav>

    <aside class="sidebar">
      <h2 style="left:19px;top:346px;">Menu</h2>
      <nav class="menu">
        <div class="active-bg"></div>
        <a href="#" style="left:26px;top:393px;">Home</a>
        <a href="#" style="left:26px;top:439px;">About Me</a>
        <a class="sub" href="#" style="left:33px;top:483px;">Meera</a>
        <a class="sub" href="#" style="left:33px;top:513px;">Quiet Harbour</a>
        <a href="#" style="left:26px;top:555px;">Consultation</a>
        <a href="#" style="left:26px;top:602px;">Resources</a>
        <a href="#" style="left:26px;top:648px;">Contact Me</a>
      </nav>
      <h2 style="left:19px;top:697px;">New Block</h2>
      <div class="block-text" style="top:758px;">
        <p>Enter Block content here...</p>
        <p style="margin-top:14px;">Lorem ipsum dolor sit amet, consectetur adipiscing elit. Etiam pharetra, tellus sit amet congue vulputate, nisi erat iaculis nibh, vitae feugiat sapien ante eget mauris.</p>
      </div>
    </aside>

    <main class="main">
      <div class="feature-photo" role="img" aria-label="Calm tropical lagoon with palm trees under a blue sky"></div>
      <div class="intro">
        <p>Enter Page content here...</p>
        <p>Lorem ipsum dolor sit amet, consectetur adipiscing elit. Etiam pharetra, tellus sit amet congue vulputate, nisi erat iaculis nibh, vitae feugiat sapien ante eget mauris. Aenean sollicitudin imperdiet arcu, vitae dignissim est posuere id.</p>
      </div>
      <a class="read-more" href="#">Read more</a>
      <ul class="points">
        <li>Suspendisse pharetra auctor pharetra. Nunc a sollicitudin est.</li>
        <li>Donec vel neque in neque porta venenatis sed sit amet lectus.</li>
        <li>Curabitur ullamcorper gravida felis, sit amet scelerisque lorem iaculis sed.</li>
      </ul>
      <svg class="quote-mark" width="30" height="40" aria-hidden="true">
        <path d="M2 4 h10 l-4 14 h4 v10 h-10 z M16 4 h10 l-4 14 h4 v10 h-10 z" fill="#7fbf4f"/>
        <rect x="2" y="30" width="24" height="8" fill="#cfe9b8"/>
      </svg>
      <blockquote class="quote">Nunc a sollicitudin est. Curabitur ullamcorper gravida felis, sit amet scelerisque lorem iaculis sed. Donec vel neque in neque porta venenatis sed sit amet lectus.</blockquote>
    </main>

    <footer class="footer">
      <span class="feed-icon" aria-hidden="true"></span>
      <p><a href="#">Link1</a> | <a href="#">Link2</a> | <a href="#">Link3</a></p>
      <p>Copyright © Ravi Tan</p>
    </footer>
  </div>

  <svg class="notes" width="1156" height="1200" aria-hidden="true">
    <ellipse cx="107" cy="534" rx="56" ry="18" fill="none" stroke="var(--note)" stroke-width="2.5"/>
    <path d="M299 668 L246 515" stroke="var(--note)" stroke-width="2.5" fill="none"/>
    <path d="M238 545 L246 515 L262 541" stroke="var(--note)" stroke-width="2.5" fill="none"/>
  </svg>
</body>
</html>
```